WP website design (Brisden)

We need a wordpress design for an established auction and real estate company based in Kentucky. The winning design will incorporate a professional color scheme with company logo in a clean layout with specified widgets. The design needs to consider that this will be developed on a responsive theme. Color is #307d84, with gray/black or other as an accent/highlight color.

Industry/Entity Type

Real Estate

Requirements
Must have
• Elelments of design need to consider that this site is going to be developed on a responsive theme.

Navigation:
1) Home 2) Current Auctions 3) Past Auctions 4) Meet the Staff 5) For Sellers 6) For Buyers 7) Testimonials 8) Contact Us

Colors will be the blue of logo plus black/gray or other accent color.

Slideshow will be prominent, please use stock real estate photo for initial image. Will have following in either header or sidebar: testimonials, social icons (FB, linkedin Twitter, RSS), Featured Auctions widget, newsletter signup form.

Footer will have contact info (below) and attached affiliation logos.
Brisden Auctions, Inc.
48710 Pomeroy Rd., Louisville KY 40199
dan.office@brisdenbid.example
Phone: (502) 555 0172

```html
<!DOCTYPE html>
<html lang="en">
<head>
<meta charset="utf-8">
<title>Brisden Auctions, Inc.</title>
<link href="https://fonts.googleapis.com/css2?family=Noto+Serif:ital,wght@0,400;0,700;1,400;1,700&display=swap" rel="stylesheet">
<style>
:root{
  --teal:#307d84;
  --ink:#333;
  --muted:#777;
  --line:#ddd;
  --page:#efefef;
  --footer:#e2e2e2;
  --footer-bar:#d3d3d3;
  --white:#fff;
  --gold:#f2c14e;
}
*{box-sizing:border-box;margin:0;padding:0}
html,body{width:806px;height:1200px;overflow:hidden}
body{font-family:"Noto Serif",serif;color:var(--ink);background:var(--page);position:relative;font-size:9px}
.abs{position:absolute}
.header{left:0;top:0;width:806px;height:358px;background:var(--white);border-top:2px solid var(--gold)}
.brand{left:56px;top:18px;width:150px;height:52px;display:flex;align-items:center;gap:6px}
.brand-mark{width:12px;height:12px;background:var(--teal);flex:none}
.brand-name{font-size:17px;font-weight:700;color:var(--teal);line-height:1.1;white-space:nowrap}
.tagline{left:222px;top:17px;width:360px;text-align:center;font-size:12px;font-style:italic;font-weight:700;color:var(--teal);white-space:nowrap}
.contact-top{left:580px;top:9px;width:176px;text-align:right;font-size:11px;line-height:17px;white-space:nowrap}
.contact-top b{font-style:italic;color:var(--teal)}
.contact-top .mail{font-style:italic;font-size:9.5px;color:#555}
.nav{left:206px;top:51px;width:556px;height:34px;background:var(--teal);display:flex;align-items:center;padding-left:11px;gap:14.5px}
.nav a{color:var(--white);text-decoration:none;font-size:11.5px}
.nav a.active{color:var(--gold)}
.hero{left:45px;top:85px;width:717px;height:273px;border:3px solid var(--teal);background:linear-gradient(180deg,#4f8fd6 0%,#9cc4ec 35%,#8a96a3 55%,#6f8a4f 78%,#456b2e 100%)}
.panel{left:48px;top:358px;width:712px;height:648px;background:var(--white)}
.h2{font-size:14px;font-weight:400;color:var(--teal);text-transform:uppercase;letter-spacing:.2px}
.welcome-title{left:63px;top:376px}
.welcome-text{left:62px;top:402px;width:498px;font-size:8.8px;line-height:14px;color:var(--muted)}
.featured-title{left:63px;top:471px;width:503px;padding-bottom:5px;border-bottom:1px solid var(--line)}
.card{left:62px;width:505px;height:154px;border:1px solid var(--line);background:var(--white)}
.card .photo{position:absolute;left:8px;top:7px;width:160px;height:140px}
.card .info{position:absolute;left:181px;top:5px;width:314px}
.card .title{font-size:10.5px;font-weight:700;color:var(--teal);line-height:14px;text-transform:uppercase}
.card .addr{position:absolute;right:0;top:0;width:120px;text-align:right;font-size:9px;line-height:14px;color:#555}
.card .sub{margin-top:10px;font-size:9px;font-style:italic}
.btn{display:inline-block;background:var(--teal);color:var(--white);font-size:9px;font-weight:700;padding:5px 8px;text-decoration:none}
.card .bids{position:absolute;right:2px;top:38px}
.card .desc{margin-top:13px;font-size:8.8px;line-height:14px;width:314px}
.card .date{position:absolute;left:181px;top:107px;width:314px;border-top:1px solid var(--line);height:46px}
.card .date .lbl{position:absolute;left:0;top:5px;font-size:13px}
.card .date .when{position:absolute;left:0;top:25px;font-size:9px}
.card .date .view{position:absolute;right:0;top:6px;border-left:1px solid var(--line);height:40px;width:105px;padding-left:13px;padding-top:2px}
.side-title{left:588px;top:376px}
.newsletter{left:588px;top:400px;width:156px;height:166px;border:1px solid var(--line);padding:7px 8px;font-size:8.5px}
.newsletter label{display:block;margin-bottom:3px}
.newsletter .field{height:21px;border:1px solid #ccc;margin-bottom:10px}
.newsletter .select{display:flex;justify-content:space-between;align-items:center;padding:0 7px;font-size:8.5px}
.caret{width:0;height:0;border-left:4px solid transparent;border-right:4px solid transparent;border-top:4px solid #444}
.testi{left:588px;top:581px;width:156px;height:150px;background:#eee}
.testi .head{height:26px;background:var(--teal);color:var(--white);font-size:14px;padding:4px 6px;text-transform:uppercase}
.testi .avatar{position:absolute;left:8px;top:34px;width:53px;height:50px;background:linear-gradient(180deg,#9ec3e3,#4b6fa8)}
.testi .who{position:absolute;left:69px;top:36px;font-size:8.5px;line-height:14px}
.testi .who b{font-size:11px;font-weight:400;color:var(--teal)}
.testi .quote{position:absolute;left:8px;top:90px;width:142px;font-size:8px;line-height:14px;color:#555}
.testi .arrow{position:absolute;top:133px;width:15px;height:15px;color:var(--white);font-size:9px;text-align:center;line-height:15px}
.testi .prev{left:2px;background:#444}
.testi .next{right:0;background:var(--teal)}
.badges{left:588px;top:747px;width:156px;height:238px;border:1px solid var(--line);background:var(--white)}
.badge{position:absolute;background:#2a2a2a}
.footer{left:0;top:1006px;width:806px;height:158px;background:var(--footer)}
.fcol{position:absolute;top:0;height:158px;border-right:1px solid #cfcfcf}
.fcol h3{position:absolute;left:0;top:10px;font-size:12.5px;font-weight:400;color:var(--teal);padding-bottom:5px;border-bottom:1px solid #c8c8c8;text-transform:uppercase;width:92px}
.fcol ul{position:absolute;left:0;top:40px;list-style:none;font-size:8.8px;line-height:16.3px}
.fcol li.dot::before{content:"";display:inline-block;width:5px;height:5px;border:1px solid #444;margin-right:6px;vertical-align:1px}
.fcol li.dot.on{color:var(--teal)}
.fcol li.dot.on::before{border-color:var(--teal)}
.social li{display:flex;align-items:center;gap:9px;height:21.2px}
.social .sq{width:16px;height:16px;background:#555}
.contact li{display:flex;gap:10px;font-size:9px;line-height:14px}
.bar{left:0;top:1164px;width:806px;height:36px;background:var(--footer-bar);display:flex;align-items:center;justify-content:center;gap:8px;font-size:9px}
.bar .mini{font-size:11px;font-weight:700;color:var(--teal)}
</style>
</head>
<body>
<header class="abs header">
  <div class="abs brand"><span class="brand-mark"></span><span class="brand-name">BRISDEN<br>AUCTIONS inc.</span></div>
  <p class="abs tagline">Did you ever wonder why Jungo didn’t have a beard?</p>
  <div class="abs contact-top"><div><b>Toll free:</b> (502) 555-0172</div><div class="mail">
    <svg width="11" height="8" viewBox="0 0 11 8" style="vertical-align:-1px"><rect width="11" height="8" fill="#307d84"/><path d="M0 0l5.5 4.5L11 0" stroke="#fff" fill="none"/></svg>
    auctions@brisdenbid.example</div></div>
  <nav class="abs nav">
    <a class="active" href="#">Home</a><a href="#">Auctions</a><a href="#">Meet the Staff</a><a href="#">For Sellers</a><a href="#">For Buyers</a><a href="#">For Realtors</a><a href="#">Classifies</a><a href="#">Contact</a>
  </nav>
  <div class="abs hero" role="img" aria-label="Row of suburban two-storey houses with lawns under a blue sky"></div>
</header>

<main class="abs panel"></main>
<h2 class="abs h2 welcome-title">Welcome to Brisden Auctions Inc.</h2>
<p class="abs welcome-text">Lorem ipsum dolor sit amet, consectetur adipiscing elit. Nam aliquet et elit vel tincidunt. Phasellus ac eros ac ligula uctor dapibus vel at sapien. Morbi vestibulum arcu eget varius tincidunt. Maecenas non posuere magna, id pharetra tortorin augue magnaLorem ipsum dolor sit amet, consectetur adipiscing elit. Nam aliquet et elit vel tincidunt.</p>
<h2 class="abs h2 featured-title">Featureds Auctions</h2>

<article class="abs card" style="top:502px">
  <div class="photo" role="img" aria-label="Storefront of an antique mall at dusk" style="background:linear-gradient(180deg,#6b7480,#3e4a4f 55%,#2d3130)"></div>
  <div class="info">
    <div class="title">Absolute Online Only Auction<br>Antiques and Collectibles</div>
    <div class="addr">5120 Harlan Rd.,<br>Louisville, KY</div>
    <div class="sub">(Bluegrass Row Antique Hall in our online auction room)</div>
    <a class="btn bids" href="#">View Bids</a>
    <div class="desc">Sterling Silver Mint Julep Cups, Larkin Pottery, Ridge Pottery, antiques, furniture, art, Pressed Glass Collection, Collegiate Items and more</div>
  </div>
  <div class="date"><span class="lbl">Auction Date</span><span class="when">Tuesday, June 24, 2014 7:00 PM</span><div class="view"><a class="btn" href="#">View Auctaion</a></div></div>
</article>

<article class="abs card" style="top:666px">
  <div class="photo" role="img" aria-label="White cargo van beside a yellow forklift" style="background:linear-gradient(180deg,#4c7a3a,#b9bcb6 45%,#8d8f88)"></div>
  <div class="info">
    <div class="title">Absolute Online Only Auction<br>Personal Property</div>
    <div class="addr">Ashbury Valley/<br>Linden Hill area</div>
    <div class="sub">Ashbury Valley/Linden Hill area</div>
    <a class="btn bids" href="#">View Bids</a>
    <div class="desc">Seller is downsizing and has asked us to auction nearly all the contents of her 2,000 sq.ft. home. Some very unique items, along with bed amd</div>
  </div>
  <div class="date"><span class="lbl">Auction Date</span><span class="when">Thursday, July 10, 2014 &nbsp;7:00 pm</span><div class="view"><a class="btn" href="#">View Auctaion</a></div></div>
</article>

<article class="abs card" style="top:829px">
  <div class="photo" role="img" aria-label="Old weathered black railway express trunk" style="background:linear-gradient(180deg,#8d8a82,#3a342b 40%,#26211a)"></div>
  <div class="info">
    <div class="title">Absolute Online Auction<br>Real Estate – Commercial</div>
    <div class="addr">9418 Corwin Rd., Louisville,<br>KY &nbsp;40291</div>
    <div class="sub">Brisden Auctions inc</div>
    <a class="btn bids" href="#">View Bids</a>
    <div class="desc">Clean, 7,200 sq. ft. free-standing building located in Marlow anchored shopping center near other major fast food, retail, and bank busi and</div>
  </div>
  <div class="date"><span class="lbl">Auction Date</span><span class="when">Thursday, July 17, 2014 &nbsp;&nbsp;1:00 pm</span><div class="view"><a class="btn" href="#">View Auctaion</a></div></div>
</article>

<h2 class="abs h2 side-title">Join Mailing List</h2>
<form class="abs newsletter">
  <label>Name</label><div class="field"></div>
  <label>E-mail Address:</label><div class="field"></div>
  <label>Choose a Newsletter:</label><div class="field select"><span>Auctions:</span><span class="caret"></span></div>
  <span class="btn">Submit</span>
</form>

<section class="abs testi">
  <div class="head">Testimonials</div>
  <div class="avatar" role="img" aria-label="Portrait of a client"></div>
  <div class="who"><b>PaulReed</b><br><span style="color:#666">(Sr. Attorney)</span><br>Posted by admin</div>
  <p class="quote">Lorem ipsum dolor sit ameconse ctetur adipNam dictum pretium odio quis tincidunt.eu,.</p>
  <span class="arrow prev">‹</span><span class="arrow next">›</span>
</section>

<section class="abs badges" aria-label="Affiliations">
  <div class="badge" style="left:16px;top:16px;width:126px;height:62px;border-radius:50%"></div>
  <div class="badge" style="left:16px;top:88px;width:52px;height:64px"></div>
  <div class="badge" style="left:84px;top:88px;width:50px;height:64px"></div>
  <div class="badge" style="left:16px;top:162px;width:56px;height:60px"></div>
  <div class="badge" style="left:90px;top:162px;width:48px;height:60px"></div>
</section>

<footer class="abs footer">
  <div class="fcol" style="left:48px;width:136px">
    <h3>Brisden</h3>
    <ul><li class="dot on">Home</li><li class="dot">About Us</li><li class="dot">Auctions Calender</li><li class="dot">Past Auctions</li><li class="dot">Meet the Staff</li><li class="dot">Testimonilas</li><li class="dot">Contact Us</li></ul>
  </div>
  <div class="fcol" style="left:228px;width:132px">
    <h3>Information</h3>
    <ul><li>For Sellers</li><li>For Buyers</li><li>for Realtors</li><li>Calssificies</li><li>Auction Process</li><li>Benifit Auction</li><li>Privacy Policy</li></ul>
  </div>
  <div class="fcol" style="left:404px;width:136px">
    <h3>Social Media</h3>
    <ul class="social" style="top:41px"><li><span class="sq"></span>friendlist</li><li><span class="sq"></span>Chirper</li><li><span class="sq"></span>Workedin</li><li><span class="sq"></span>Circles +</li><li><span class="sq"></span>Pinwall</li></ul>
  </div>
  <div class="fcol" style="left:584px;width:180px;border:none">
    <h3>Contact Us</h3>
    <ul class="contact" style="top:42px">
      <li style="height:56px"><svg width="12" height="16" viewBox="0 0 12 16"><path d="M6 15C2 10 1 8 1 6a5 5 0 0110 0c0 2-1 4-5 9z" fill="none" stroke="#444" stroke-width="1.4"/><circle cx="6" cy="6" r="1.8" fill="#444"/></svg><span>Dan Brisden, Tom Keller, Anna Ross, Ray Mercer</span></li>
      <li style="height:40px"><svg width="12" height="14" viewBox="0 0 12 14"><path d="M3 1l2 3-1.5 1.5c.7 2 2 3.3 4 4L9 8l3 2-1.5 3C5 12 1 7 1 2z" fill="none" stroke="#444" stroke-width="1.2"/></svg><span>(502) 555-0172</span></li>
      <li><svg width="14" height="12" viewBox="0 0 14 12"><rect x="1" y="2" width="12" height="9" fill="none" stroke="#444" stroke-width="1.3"/><path d="M1 2l6 5 6-5" fill="none" stroke="#444" stroke-width="1.3"/></svg><span>auctions@brisdenbid.example</span></li>
    </ul>
  </div>
</footer>
<div class="abs bar"><span class="mini">BRISDEN</span><span>Copyright © 2014 by brisdenauctions inc. All Rights Reserved</span></div>
</body>
</html>
```